Hi! We require a design for business cards for directors and head teachers of an international daycare for children 0 - 9. We are family-owned, -operated and -oriented. We have six locations, looking to franchise. Our USPs are: 1) Flexibility 2) Quality teachers 3) International culture 4) Best nutrition We are quality teachers and professional caretakers, but with creativity and personality! Business cards should be playful (but no Comic Sans or baby hand prints), colorful (but no rainbows), and have some breathing space. It should be obvious from the business card that we're a daycare. In 2020 we'll be launching our new website based on this design: https://plomvane.io/47K2RQLWZTD The font in the new website will be Houschka (medium, demibold, bold). We will keep our current logo, included in the files here. There are also screenshots of some designs we like. Show us your best! :)

Industry/Entity Type

Childcare

Contact Information for Business Card

Lotte de Vries-Bakhuis
Communications Wizard
Poppel Hoek International Daycare
Kastanjeweg 47 B, 2316 KR Leiden
www.poppelhoek.nl
+31 647315082

Font styles to use
Serif
Sans Serif

Colors

Designer to choose colors to be used in the design.

Requirements
Must have
• Color

```html
<!DOCTYPE html>
<html lang="en">
<head>
<meta charset="utf-8">
<title>Poppel Hoek – Business Card</title>
<link rel="stylesheet" href="https://fonts.googleapis.com/css2?family=Montserrat:wght@400;500;600;700;800&family=Oswald:wght@600&display=swap">
<style>
  :root {
    --pink: #e84a83;
    --blue: #08ade0;
    --blue-soft: #8fd8f2;
    --pink-soft: #f6b9cf;
    --ink: #1c1c1c;
    --paper: #ffffff;
    --backdrop: #2a2a2a;
  }
  * { margin: 0; padding: 0; box-sizing: border-box; }
  html, body { width: 1200px; height: 1200px; overflow: hidden; }
  body {
    background: var(--backdrop);
    font-family: "Montserrat", sans-serif;
    position: relative;
  }
  .card {
    position: absolute;
    width: 620px;
    height: 360px;
    background: var(--paper);
    border-radius: 26px;
    overflow: hidden;
    box-shadow: 0 18px 40px rgba(0,0,0,.55);
  }
  .card--front { left: 70px; top: 130px; }
  .card--back { left: 510px; top: 660px; }

  .pattern-fill {
    position: absolute; inset: 0;
    background:
      radial-gradient(ellipse 48% 42% at 50% 50%, #ffffff 0%, rgba(255,255,255,.9) 55%, rgba(255,255,255,0) 100%),
      linear-gradient(135deg, var(--blue-soft) 0%, var(--pink-soft) 35%, #ffffff 50%, var(--blue-soft) 70%, var(--pink-soft) 100%);
  }
  .brand-name {
    font-family: "Montserrat", sans-serif;
    font-weight: 800;
    color: var(--pink);
    text-transform: uppercase;
    letter-spacing: .5px;
    line-height: 1;
    display: flex; align-items: center; gap: 12px;
  }
  .brand-name .brand-dot {
    width: 18px; height: 18px; border-radius: 50%; background: var(--blue);
  }
  .card--front .brand-name {
    position: absolute; left: 50%; top: 50%;
    transform: translate(-50%, -50%);
    font-size: 54px;
    white-space: nowrap;
  }
  .card--back .brand-name {
    position: absolute; right: 40px; top: 80px;
    font-size: 36px;
  }

  .contact-lines {
    position: absolute; right: 44px; top: 172px;
    font-size: 12px; font-weight: 500; color: var(--ink);
    text-align: right; line-height: 22px;
  }
  .contact-lines .web-accent { color: var(--blue); }
  .contact-lines svg { width: 12px; height: 12px; vertical-align: -2px; margin-left: 5px; }

  .divider {
    position: absolute; left: 60px; right: 36px; top: 236px;
    height: 1.5px; background: var(--pink);
  }
  .person-name {
    position: absolute; left: 52px; top: 188px;
    font-family: "Oswald", sans-serif; font-weight: 600;
    font-size: 26px; color: var(--pink); text-transform: uppercase;
    letter-spacing: -.2px; line-height: 1;
  }
  .person-title {
    position: absolute; left: 58px; top: 218px;
    font-size: 12px; color: var(--ink); font-weight: 400;
  }
  .company {
    position: absolute; left: 62px; top: 246px;
    font-size: 13px; font-weight: 700; color: var(--blue);
  }
  .address {
    position: absolute; left: 62px; top: 266px;
    font-size: 12px; font-weight: 500; color: var(--ink);
    display: flex; align-items: center; gap: 5px;
  }
  .address svg { width: 10px; height: 12px; }
  .footer-bands { position: absolute; left: 0; bottom: 0; width: 620px; height: 80px; }
</style>
</head>
<body>

  <section class="card card--front" aria-label="Card front">
    <div class="pattern-fill" role="img" aria-label="Playful confetti pattern of pink triangles, blue dots and grey dashes"></div>
    <div class="brand-name"><span class="brand-dot"></span>Poppel Hoek</div>
  </section>

  <section class="card card--back" aria-label="Card back">
    <div class="brand-name"><span class="brand-dot"></span>Poppel Hoek</div>

    <div class="contact-lines">
      <div>+31 647315082
        <svg viewBox="0 0 24 24" fill="var(--blue)"><path d="M6.6 10.8a15.1 15.1 0 0 0 6.6 6.6l2.2-2.2c.3-.3.7-.4 1-.2 1.1.4 2.3.6 3.6.6.6 0 1 .4 1 1V20c0 .6-.4 1-1 1A17 17 0 0 1 3 4c0-.6.4-1 1-1h3.5c.6 0 1 .4 1 1 0 1.3.2 2.5.6 3.6.1.3 0 .7-.2 1z"/></svg>
      </div>
      <div>www.<span class="web-accent">poppelhoek</span>.nl
        <svg viewBox="0 0 24 24" fill="none" stroke="var(--blue)" stroke-width="2.2"><circle cx="12" cy="12" r="9"/><path d="M3 12h18M12 3c3 3 3 15 0 18M12 3c-3 3-3 15 0 18"/></svg>
      </div>
    </div>

    <div class="person-name">Lotte de Vries-Bakhuis</div>
    <div class="person-title">Communications Wizard</div>
    <div class="divider"></div>
    <div class="company">Poppel Hoek International Daycare</div>
    <div class="address">
      <svg viewBox="0 0 20 24" fill="var(--blue)"><path d="M10 0a8 8 0 0 0-8 8c0 6 8 16 8 16s8-10 8-16a8 8 0 0 0-8-8zm0 11a3 3 0 1 1 0-6 3 3 0 0 1 0 6z"/></svg>
      Kastanjeweg 47 B, 2316 KR Leiden
    </div>

    <svg class="footer-bands" viewBox="0 0 620 80" preserveAspectRatio="none" aria-hidden="true">
      <path d="M0 58 H400 C420 58 422 34 445 34 H620 V80 H0 Z" fill="var(--blue)"/>
      <path d="M0 50 H396 C410 50 414 38 420 34 L430 34 C420 36 416 56 398 56 H0 Z" fill="var(--pink)"/>
    </svg>
  </section>

</body>
</html>
```